KRV Business Cards

We are a local commercial development company based in Silicon Valley and we would like a new business card. I've attached a copy of our company brochure to give a flavor of what we do, our logo, info company colors/graphics, and our current business card. We don't necessarily need a crazy makeover, but would like something that feels a little bit more "fresh" and modern (we've had the same business card design for 15+ years), but still in keeping with our overall brand -- clean, high-quality, modern but timeless. Would like to add our website to the info on the card (www.velmara.com) and would like the flexibility for some folks to have an efax number listed and some not to have that included (without it looking like there is a hole).

```html
<!DOCTYPE html>
<html lang="en">
<head>
<meta charset="utf-8">
<title>Velmara Development Company – Business Card</title>
<link rel="stylesheet" href="https://fonts.googleapis.com/css2?family=Cinzel:wght@400;500&family=EB+Garamond:wght@400;600&display=swap">
<style>
  :root {
    --backdrop: #6f6f72;
    --card: #f3f2ef;
    --navy: #3b5574;
    --ink: #222426;
    --rule: #b9b8b4;
  }
  * { box-sizing: border-box; margin: 0; padding: 0; }
  html, body {
    width: 1200px; height: 913px; overflow: hidden;
    background: var(--backdrop);
  }
  .canvas {
    width: 1200px; height: 913px;
    display: flex; align-items: center; justify-content: center;
  }
  .business-card {
    position: relative;
    width: 840px; height: 480px;
    background: var(--card);
    box-shadow: 0 18px 40px rgba(0,0,0,.28);
  }
  .company-name {
    position: absolute;
    left: 70px; top: 200px;
    width: 340px;
    display: flex; align-items: center; gap: 18px;
    font-family: "EB Garamond", serif;
    font-weight: 400;
    font-size: 27px;
    line-height: 1.15;
    color: var(--navy);
  }
  .company-name .mark {
    flex: none;
    width: 26px; height: 26px;
    background: var(--navy);
  }
  .divider {
    position: absolute;
    left: 440px; top: 0; bottom: 0;
    border-left: 1px solid var(--rule);
  }
  .details {
    position: absolute;
    left: 472px; top: 64px;
    font-family: "EB Garamond", serif;
    color: var(--ink);
  }
  .person-name {
    font-family: "Cinzel", serif;
    font-weight: 500;
    font-size: 27px;
    letter-spacing: .5px;
  }
  .person-title {
    font-family: "Cinzel", serif;
    font-size: 13px;
    letter-spacing: 1px;
    margin-top: -2px;
  }
  .address {
    margin-top: 34px;
    font-size: 19px;
    line-height: 1.2;
  }
  .contact {
    margin-top: 48px;
    font-size: 19px;
    line-height: 1.22;
    list-style: none;
  }
  .contact .label { font-weight: 600; display: inline-block; width: 22px; }
</style>
</head>
<body>
<main class="canvas">
  <article class="business-card">
    <div class="company-name">
      <span class="mark"></span>
      <span>Velmara Development<br>Company, LLC</span>
    </div>
    <div class="divider"></div>
    <section class="details">
      <h1 class="person-name">Irene T. Halden</h1>
      <p class="person-title">PARTNER</p>
      <p class="address">388 Corwin Avenue, Palo Alto,<br>California 94301</p>
      <ul class="contact">
        <li><span class="label">M</span>650 555 0142</li>
        <li><span class="label">P</span>650 555 0177</li>
        <li><span class="label">F</span>650 555 0193</li>
        <li>irene@velmara.com</li>
        <li>www.velmara.com</li>
      </ul>
    </section>
  </article>
</main>
</body>
</html>
```